Guiding Your Revenue Overhaul *

Bold eye-catching design for business non-fiction: I am seeking a bold, and clean design for a book. The book will be 6X9 for both the ebook and in print. I am open to ideas, but found that books like “steady as rain” with contrast are highly desirable for business books.

I am open to color choices.

I would also like a growth orientated graphic in the book - something to show growth, leadership, movement. Not just a plain graphic.

The title:

Guiding Your Revenue Overhaul

The subtitle - I am open to suggestions. Two subtitles I am considering:

A framework for new sales leaders and those who want to keep winning.

A guide for new sales leaders and those who want to keep winning.

The below is an introduction of the book: (Back Jacket)

Sales transformation is a topic that is infrequently written about. For the new sales leader, there are a myriad of books written on coaching, leadership, forecasting, solution selling and sales process but very little is written about how to assess a sales team and build a plan for long-term success.

Through my sales leadership career, whether recently promoted or starting with a new team, I have often asked the question: Where do I start?

In the end, I was disappointed with the answers from currently available books and research, left to figure it out myself - which I did over a decade, with great pain and through many transformations. The inability to answer the question – Where do I start? – is why I wrote this book. To answer that question.

The goal of this book is to help sales leaders answer that question by providing a framework to understand the business, build a plan, and guide the team through the different stages of a sales transformation. A framework to succeed at the fastest pace possible, quarter after quarter.

(End back jacket - the rest is just additional context)

Over the last decade, I have had the privilege of leading teams in North America, Europe, and Asia. I have led turnarounds, growth businesses, and realignments. Each team was different in size, complexity, and culture; and each one offered up new and unique challenges. Each team operated with different market dynamics: one was a commodity; one was a low-cost leader; one was a market innovator. Each transformation helped me learn by taking risks, by failing and by succeeding. At each step, I had many teachers; and as I learned, I made notes. Over time I built a framework that you can leverage as you read and absorb this book. As you lead your team through a sales transformation.

I hope that this book will become for you what The Copper Lantern is for me: a favorite on your bookshelf; underlined, highlighted, dog-eared, and an ongoing reference.

Sales leadership is a journey. It is never linear, and it is always changing. At different times, different parts of this book will apply, while others will not, but hopefully, you will find it a useful and long-lasting reference.

Target Market(s)

Business readers. Sales leaders.

Requirements
Must have
• Modern, clear, eye catching colours. Clean. Graphics that indicate growth, leadership, strength.
• Please ensure the design has the full cover and back jacket design. Please use the introduction of the book as the back jacket text.

```html
<!DOCTYPE html>
<html lang="en">
<head>
<meta charset="utf-8">
<title>Guiding Your Revenue Overhaul — Cover</title>
<link rel="stylesheet" href="https://fonts.googleapis.com/css2?family=Oswald:wght@600;700&family=Open+Sans:wght@400&family=Jost:wght@400&display=swap">
<style>
  :root {
    --ink-green: #3b4533;
    --body-ink: #2b2b2b;
    --sub-brown: #6a4e1e;
    --paper: #ffffff;
    --paper-shade: #ececec;
    --leaf-light: #a6dc3c;
    --leaf-mid: #7cc224;
    --leaf-deep: #4e8f17;
  }
  * { margin: 0; padding: 0; box-sizing: border-box; }
  html, body { width: 1200px; height: 859px; overflow: hidden; background: var(--paper); }
  .cover {
    position: relative;
    width: 1200px; height: 859px;
    background: linear-gradient(180deg, var(--paper) 0%, var(--paper) 70%, var(--paper-shade) 100%);
    overflow: hidden;
  }
  .back-jacket {
    position: absolute; left: 42px; top: 44px; width: 481px;
  }
  .back-title {
    font-family: "Oswald", sans-serif; font-weight: 700;
    font-size: 21px; letter-spacing: 0.6px; color: var(--ink-green);
    text-align: center; margin-bottom: 20px;
  }
  .back-copy p {
    font-family: "Open Sans", sans-serif; font-size: 15px; line-height: 21.6px;
    color: var(--body-ink); text-align: justify; margin-bottom: 21px;
  }
  .spine, .front-title { position: absolute; }
  .spine { left: 548px; top: 0; width: 72px; height: 859px; }
  .front-title { left: 640px; top: 0; width: 540px; height: 420px; }
  .title-type { font-family: "Oswald", sans-serif; font-weight: 700; fill: var(--ink-green); }
  .spine-author { font-family: "Jost", sans-serif; font-weight: 400; fill: var(--body-ink); }
  .subtitle {
    position: absolute; left: 640px; top: 343px; width: 536px;
    font-family: "Jost", sans-serif; font-size: 22.5px; line-height: 27px;
    color: var(--sub-brown); text-align: center; text-transform: uppercase; letter-spacing: 0.2px;
  }
  .growth-graphic {
    position: absolute; left: 815px; top: 400px; width: 230px; height: 385px;
    border-radius: 40% 40% 8px 8px;
    background: radial-gradient(ellipse at 50% 40%, var(--leaf-light) 0%, var(--leaf-mid) 55%, var(--leaf-deep) 100%);
    opacity: 0.85;
  }
  .author-name {
    position: absolute; left: 640px; top: 806px; width: 536px;
    font-family: "Jost", sans-serif; font-size: 30px; letter-spacing: 2.5px;
    color: var(--body-ink); text-align: center;
  }
</style>
</head>
<body>
<main class="cover">
  <section class="back-jacket">
    <h2 class="back-title">GUIDING YOUR REVENUE OVERHAUL</h2>
    <div class="back-copy">
      <p>Sales transformation is a topic that is infrequently written about. For the new sales leader, there are a myriad of books written on coaching, leadership, forecasting, solution selling and sales process but very little is written about how to assess a sales team and build a plan for long-term success.</p>
      <p>Through my sales leadership career, whether recently promoted or starting with a new team, I have often asked the question: Where do I start?</p>
      <p>In the end, I was disappointed with the answers from currently available books and research, left to figure it out myself - which I did over a decade, with great pain and through many transformations. The inability to answer the question – Where do I start? – is why I wrote this book. To answer that question.</p>
      <p>The goal of this book is to help sales leaders answer that question by providing a framework to understand the business, build a plan, and guide the team through the different stages of a sales transformation. A framework to succeed at the fastest pace possible, quarter after quarter.</p>
    </div>
  </section>

  <svg class="spine" viewBox="0 0 72 859" aria-label="Spine">
    <text class="title-type" transform="translate(28 50) rotate(90)" font-size="25" textLength="472" lengthAdjust="spacingAndGlyphs">GUIDING YOUR REVENUE OVERHAUL</text>
    <text class="spine-author" transform="translate(29 640) rotate(90)" font-size="24" textLength="176" lengthAdjust="spacingAndGlyphs">AUTHOR NAME</text>
  </svg>

  <svg class="front-title" viewBox="0 0 540 420" aria-label="Guiding Your Revenue Overhaul">
    <text class="title-type" x="20" y="126" font-size="120" textLength="496" lengthAdjust="spacingAndGlyphs">GUIDING YOUR</text>
    <text class="title-type" x="24" y="280" font-size="172" textLength="488" lengthAdjust="spacingAndGlyphs">REVENUE</text>
    <text class="title-type" x="24" y="330" font-size="54" textLength="492" lengthAdjust="spacingAndGlyphs">OVERHAUL</text>
  </svg>

  <p class="subtitle">A framework for new sales leaders<br>and those who want to keep winning</p>

  <div class="growth-graphic" role="img" aria-label="Illustration: a green tree made of upward branching arrows growing out of cracked ground"></div>

  <p class="author-name">AUTHOR NAME</p>
</main>
</body>
</html>
```